VELOTRA Brisbane Tiling Service

My name is Milos Vrenbek i need a business card for a new company. We are wall and floor tilers based in Brisbane, our company is Velotra Brisbane Tiling Service.
We would like a logo from our website used on our cards. Our website is www.velotra-tiles.com.au

I would like my Facebook and Twitter accounts on my card.

Business

Colors
0692cd
3176b5
33a6d7
85cae6

```html
<!DOCTYPE html>
<html lang="en">
<head>
<meta charset="utf-8">
<title>Velotra Brisbane Tiling Service – Business Card</title>
<link rel="stylesheet" href="https://fonts.googleapis.com/css2?family=Open+Sans:wght@400;600&display=swap">
<style>
  :root {
    --blue-deep: #3176b5;
    --blue-strong: #0692cd;
    --blue-mid: #33a6d7;
    --blue-light: #85cae6;
    --card-white: #f7f9fb;
    --card-tint: #e4eef5;
    --ink: #2b2f33;
    --stage: #ececec;
  }
  * { box-sizing: border-box; margin: 0; padding: 0; }
  html, body { width: 1200px; height: 1000px; overflow: hidden; }
  body {
    background: var(--stage);
    font-family: "Open Sans", Arial, sans-serif;
    position: relative;
  }
  .card {
    position: absolute;
    width: 630px;
    height: 360px;
    overflow: hidden;
    box-shadow: 0 2px 6px rgba(0,0,0,0.12);
  }
  .card-surface {
    position: absolute;
    inset: 0;
    background: linear-gradient(135deg, var(--card-white) 0%, var(--card-tint) 100%);
  }
  .card-front { left: 70px; top: 80px; }
  .card-back { left: 500px; top: 560px; }

  .brand {
    position: absolute;
    display: flex;
    align-items: center;
    gap: 22px;
  }
  .brand-square {
    background: linear-gradient(135deg, var(--blue-light), var(--blue-strong));
    border-radius: 6px;
    flex: none;
  }
  .brand-name {
    color: var(--blue-mid);
    font-weight: 400;
    line-height: 1.05;
  }
  .card-front .brand { left: 60px; top: 78px; }
  .card-front .brand-square { width: 120px; height: 120px; }
  .card-front .brand-name { font-size: 44px; }
  .website {
    position: absolute;
    left: 222px;
    bottom: 48px;
    color: var(--blue-mid);
    font-size: 30px;
  }

  .card-back .brand { right: 44px; top: 26px; gap: 14px; }
  .card-back .brand-square { width: 62px; height: 62px; }
  .card-back .brand-name { font-size: 22px; }
  .contact-list {
    position: absolute;
    left: 36px;
    top: 30px;
    list-style: none;
    font-size: 15px;
    color: var(--ink);
    line-height: 1.5;
  }
  .contact-list li { display: flex; align-items: center; gap: 8px; }
  .icon { width: 16px; height: 16px; flex: none; }
  .name-band {
    position: absolute;
    left: 0; right: 0;
    top: 130px;
    height: 96px;
    background: linear-gradient(90deg, var(--blue-deep), var(--blue-mid));
    display: flex;
    align-items: center;
    justify-content: center;
  }
  .person-name {
    color: #ffffff;
    font-size: 40px;
    font-weight: 400;
    letter-spacing: 0.5px;
  }
  .social-list {
    position: absolute;
    left: 150px;
    top: 258px;
    list-style: none;
    font-size: 16px;
    color: var(--ink);
    line-height: 1.9;
  }
  .social-list li { display: flex; align-items: center; gap: 10px; }
  .social-mark {
    width: 20px; height: 20px;
    background: var(--blue-strong);
    border-radius: 3px;
    flex: none;
  }
</style>
</head>
<body>
  <section class="card card-front">
    <div class="card-surface" role="img" aria-label="Soft pale blue tile grid background"></div>
    <div class="brand">
      <div class="brand-square"></div>
      <div class="brand-name">Velotra<br>Brisbane Tiling<br>Service</div>
    </div>
    <p class="website">www.velotra-tiles.com.au</p>
  </section>

  <section class="card card-back">
    <div class="card-surface" role="img" aria-label="Soft pale blue tile grid background"></div>
    <ul class="contact-list">
      <li>
        <svg class="icon" viewBox="0 0 16 16" aria-hidden="true">
          <rect x="0" y="0" width="16" height="16" rx="2" fill="var(--blue-strong)"/>
          <rect x="3" y="5" width="10" height="7" fill="none" stroke="#fff" stroke-width="1.2"/>
          <path d="M3 5 L8 9 L13 5" fill="none" stroke="#fff" stroke-width="1.2"/>
        </svg>
        info@velotra-tiles.com.au
      </li>
      <li>
        <svg class="icon" viewBox="0 0 16 16" aria-hidden="true">
          <rect x="0" y="0" width="16" height="16" rx="2" fill="var(--blue-strong)"/>
          <rect x="5" y="3" width="6" height="10" rx="1" fill="none" stroke="#fff" stroke-width="1.2"/>
        </svg>
        0412 555 018
      </li>
      <li>
        <svg class="icon" viewBox="0 0 16 16" aria-hidden="true">
          <rect x="0" y="0" width="16" height="16" rx="2" fill="var(--blue-strong)"/>
          <path d="M4 4 h3 l1 3 -1.5 1 a6 6 0 0 0 2.5 2.5 l1-1.5 3 1 v3 a9 9 0 0 1 -9 -9z" fill="#fff"/>
        </svg>
        07 3555 0142
      </li>
    </ul>
    <div class="brand">
      <div class="brand-square"></div>
      <div class="brand-name">Velotra<br>Brisbane Tiling<br>Service</div>
    </div>
    <div class="name-band">
      <h1 class="person-name">Milos Vrenbek</h1>
    </div>
    <ul class="social-list">
      <li><span class="social-mark"></span>@your profile name</li>
      <li><span class="social-mark"></span>/your profile name</li>
    </ul>
  </section>
</body>
</html>
```